1 Landingpage plus 2 passende Newsletter-Templates (Responsive)
Zielgruppe
Wir sind ein deutscher E-Mail- und Clouddienstleister, unsere Zielgruppe sind in erster Linie Privatkunden.
Aufgabenstellung
Für eine noch zu startende, erfolgreiche Marketingkampagne, benötigen wir für eines unserer Produkte insgesamt zwei unterschiedliche Newsletter-Templates (A/B-Test) und eine optisch dazu passende Landingpage inkl. Registrierungsformular. Die Anbindung an unser System übernehmen wir selbst.
Newslettertemplates sowie Landingpage sollen so einfach wie möglich, dennoch werbewirksam und nach heutigen Kriterien und Maßstäben entworfen und hergestellt werden (Responsive, Beachtung gängiger E-Mailstandards und -clients).
Die Ausgestaltung von Text und Grafik sollte von jemandem durchgeführt werden, der ggfls. bereits Erfahrung im E-Mailmarketing hat.
Unser eigenes CD/CI muss eingearbeitet bzw. berücksichtigt werden, darf aber "aufgehübscht" und moderner interpretiert werden.
Zu einem späteren Zeitplunkt planen wir den Relaunch unseres Portals, ggfls. ergeben sich weitere Möglichkeiten der Zusammenarbeit.
Unser Logo kann im .SVG-Format bereit gestellt werden.

```html
<!DOCTYPE html>
<html lang="de">
<head>
<meta charset="utf-8">
<title>Nordpost Connect – Newsletter</title>
<link rel="stylesheet" href="https://fonts.googleapis.com/css2?family=Montserrat:wght@300;400;600&family=Poppins:wght@600&family=Exo+2:wght@600;700&family=Kalam:wght@400&display=swap">
<style>
  :root {
    --orange: #ec5d00;
    --orange-light: #ff5a00;
    --ink: #1e1e1e;
    --text: #2b2b2b;
    --muted: #b9bcc0;
    --page: #eceff1;
    --card: #ffffff;
    --rule: #eeeeee;
    --social: #c4c4c4;
    --cloud: #adcd5a;
    --server: #6a6d78;
    --paper: #e8ecf2;
    --pen: #8fd0ef;
    --shield-dark: #35485e;
    --check: #e94b35;
  }
  * { box-sizing: border-box; margin: 0; padding: 0; }
  html, body { width: 698px; height: 1200px; overflow: hidden; }
  body { background: var(--page); font-family: "Montserrat", sans-serif; color: var(--text); position: relative; }
  .mail-card {
    position: absolute; left: 38px; top: 30px; width: 618px; height: 1053px;
    background: var(--card); border-radius: 6px; box-shadow: 0 1px 4px rgba(0,0,0,.12);
    overflow: hidden;
  }
  .mail-header { height: 75px; background: var(--orange); position: relative; }
  .brand {
    position: absolute; left: 22px; top: 18px; width: 240px; height: 37px;
    background: var(--orange-light); border-radius: 4px;
    display: flex; align-items: center; gap: 12px; padding-left: 18px;
    white-space: nowrap;
    font-family: "Exo 2", sans-serif; font-weight: 700; font-size: 22px; line-height: 1; color: #fff;
  }
  .brand-mark { width: 12px; height: 12px; background: #fff; border-radius: 2px; flex: none; }
  .headline {
    position: absolute; top: 100px; width: 100%; text-align: center; line-height: 48px;
    font-family: "Poppins", sans-serif; font-weight: 600; font-size: 39px; color: var(--ink); letter-spacing: .5px;
  }
  .intro {
    position: absolute; top: 168px; width: 100%; text-align: center;
    font-weight: 300; font-size: 20px; line-height: 24px; color: #333;
  }
  .cta {
    position: absolute; left: 165px; top: 245px; width: 292px; height: 37px;
    background: var(--orange); box-shadow: 0 1px 3px rgba(0,0,0,.25);
    display: flex; align-items: center; justify-content: center;
    font-family: "Exo 2", sans-serif; font-weight: 600; font-size: 21px; color: #fff;
  }
  .feature-art { position: absolute; border-radius: 10px; }
  .feature-text {
    position: absolute; text-align: center; white-space: nowrap;
    font-size: 15px; line-height: 23.5px; color: var(--text);
  }
  .feature-text em { font-style: normal; font-weight: 600; color: var(--orange); }
  .divider { position: absolute; left: 45px; width: 540px; height: 2px; background: var(--rule); }
  .greeting { position: absolute; top: 893px; width: 100%; text-align: center; font-weight: 300; font-size: 20px; color: #333; }
  .signature { position: absolute; top: 918px; width: 100%; text-align: center; font-family: "Kalam", cursive; font-size: 32px; color: #111; }
  .mail-notes { position: absolute; top: 975px; width: 100%; text-align: center; font-size: 14.5px; line-height: 22px; }
  .mail-notes a { color: var(--orange); font-weight: 600; text-decoration: none; }
  .footer-links { position: absolute; left: 56px; top: 1100px; font-size: 15.5px; color: var(--orange); }
  .footer-links span.sep { margin: 0 14px; font-size: 10px; vertical-align: middle; }
  .footer-address { position: absolute; left: 56px; top: 1125px; font-size: 11.5px; font-weight: 300; color: var(--muted); }
  .social { position: absolute; top: 1101px; width: 40px; text-align: center; }
  .social-dot { width: 32px; height: 32px; border-radius: 50%; background: var(--social); margin: 0 auto; }
  .social-label { font-size: 7px; color: var(--muted); margin-top: 5px; }
</style>
</head>
<body>
  <main class="mail-card">
    <header class="mail-header">
      <div class="brand"><span class="brand-mark"></span>Nordpost Connect</div>
    </header>

    <h1 class="headline">Melden Sie sich jetzt an!</h1>
    <p class="intro">Lorem ipsum dolor sit amet, consetetur sadipscing elitr,<br>sed diam nonumy eirmod tempor invidunt ut labore et</p>
    <div class="cta">Jetzt kostenlos probieren!</div>

    <div class="feature-art" role="img" aria-label="Illustration: Server vor grüner Wolke"
         style="left:45px;top:337px;width:134px;height:133px;background:linear-gradient(180deg,var(--cloud),var(--server));"></div>
    <p class="feature-text" style="left:210px;top:384px;width:380px;">Dipscing elitr, sed diam <em>Lorem ipsum</em> dolor sit<br>amet, consetetur sadipscing elitr, sed diam</p>

    <div class="divider" style="top:493px;"></div>

    <p class="feature-text" style="left:45px;top:554px;width:375px;"><em>Lorem ipsum</em> dipscing elitr, sed diam dolor sit<br>amet, consetetur sadipscing elitr, sed diam sa-<br>dipscing elitr sadipscing elitr, sed diam</p>
    <div class="feature-art" role="img" aria-label="Illustration: Dokument mit Füllfederhalter"
         style="left:440px;top:522px;width:131px;height:134px;background:linear-gradient(135deg,var(--paper),var(--pen));"></div>

    <div class="divider" style="top:690px;"></div>

    <div class="feature-art" role="img" aria-label="Illustration: Schutzschild mit Häkchen"
         style="left:51px;top:717px;width:121px;height:139px;background:linear-gradient(160deg,var(--shield-dark),#c9ccd2 60%,var(--check));"></div>
    <p class="feature-text" style="left:195px;top:748px;width:400px;"><em>Dipscing elitr, sed</em> diam Lorem ipsum dolor sit<br>amet, consetetur <em>sadipscing</em> elitr, sed diam Dips-<br><em>cing elitr,</em> sed diam Lorem ipsum dolor sit amet,</p>

    <p class="greeting">Mit freundlichen Grüßen</p>
    <p class="signature">Ihr Nordpost Team</p>

    <p class="mail-notes"><a href="#">Klicken Sie hier</a>, wenn Sie keine weiteren Newsletter mehr erhalten wollen<br><a href="#">Sie brauchen Hilfe?</a> Wir sind für Sie jederzeit erreichbar!</p>
  </main>

  <nav class="footer-links">Über uns<span class="sep">•</span>Deabonnieren<span class="sep">•</span>Impressum</nav>
  <p class="footer-address">Lindenweg 12, 10115 Berlin, Deutschland</p>

  <div class="social" style="left:441px;"><div class="social-dot"></div><div class="social-label">Video</div></div>
  <div class="social" style="left:500px;"><div class="social-dot"></div><div class="social-label">Social</div></div>
  <div class="social" style="left:560px;"><div class="social-dot"></div><div class="social-label">News</div></div>
  <div class="social" style="left:620px;"><div class="social-dot"></div><div class="social-label">Blog</div></div>
</body>
</html>
```